Design for Pediatric Occupational Therapist who works with children with special needs

I need 2 x 2 sq business cards and post cards for my Pediatric Occupational Therapy business. We work with children with special needs and help them learn skills for daily living (eating, writing, dressing, etc). We're looking for a colorful design (not loud) that looks professional and helps it stand out from other cards. I want to avoid many of the standard designs that you see on Pella press which are used my many other Pediatric OT's. The design will be intended for business cards, post cards and hopefully can also be used on company letterhead. I'll upload a current copy of the logo we currently use on company letter head so you get an idea of the design we've been using to date. This image does not need to be used again, but serves more as a reference to the design used in the past. The winning designer will likely be hired to design a custom logo for letter head.

Target Market(s)

Families of children with special needs, pediatricians

Industry/Entity Type

Business

Contact Information for Business Card

I need a logo or design for 2 x 2 sq business cards and post cards for my Pediatric Occupational Therapy business. We work with children with special needs and help them learn skills for daily living (eating, writing, dressing, etc). We're looking for a colorful design (not loud) that looks professional and helps it stand out from other cards. I want to avoid many of the standard designs that you see on Pella press which are used my many other Pediatric OT's. The design will be intended for business cards, post cards and hopefully can also be used on company letterhead. I'll upload a current copy of the logo we currently use on company letter head so you get an idea of the design we've been using to date.

Font styles to use
Sans Serif

Requirements
Must have
• Area to include company name, address, phone, etc.
• Company name = Brightway Care Partners

```html
<!DOCTYPE html>
<html lang="en">
<head>
<meta charset="utf-8">
<title>Brightway Care Partners – Business Cards</title>
<link rel="stylesheet" href="https://fonts.googleapis.com/css2?family=Quicksand:wght@500;600;700&family=Oswald:wght@500;600&display=swap">
<style>
  :root{
    --bg:#e9ecea;
    --card:#ffffff;
    --red:#e0344a;
    --blue:#2aa3dc;
    --navy:#3a5ea8;
    --yellow:#f2cf1c;
    --orange:#ee8a22;
    --ink:#2b2b2b;
    --brand:#3c9aa6;
  }
  *{margin:0;padding:0;box-sizing:border-box}
  html,body{width:1200px;height:900px;overflow:hidden;background:var(--bg)}
  .sheet{position:relative;width:1200px;height:900px}
  .card{position:absolute;top:230px;width:440px;height:440px;background:var(--card);overflow:hidden;box-shadow:0 10px 28px rgba(0,0,0,.22)}
  .card--front{left:120px}
  .card--back{left:640px}
  .card svg.art{position:absolute;inset:0;width:440px;height:440px}
  .brand-name{position:absolute;left:0;right:0;top:120px;text-align:center;font-family:"Quicksand",sans-serif;font-weight:600;color:var(--brand);line-height:1.15}
  .brand-name .mark{display:inline-block;width:26px;height:26px;border-radius:50%;background:var(--orange);margin-bottom:18px}
  .brand-name .line1{display:block;font-size:40px;letter-spacing:8px}
  .brand-name .line2{display:block;font-size:24px;letter-spacing:1px;margin-top:6px}
  .back-title{position:absolute;left:24px;top:90px;transform:rotate(-20deg);transform-origin:left top;font-family:"Quicksand",sans-serif;font-weight:700;font-size:18px;letter-spacing:7px;color:#fff}
  .kids-area{position:absolute;left:70px;top:185px;width:300px;height:120px;border-radius:40px;background:radial-gradient(ellipse at center,rgba(238,138,34,.16),rgba(42,163,220,.08) 60%,rgba(255,255,255,0) 80%)}
  .contact{position:absolute;left:76px;top:205px;list-style:none;font-family:"Oswald",sans-serif;font-weight:600;font-size:18px;color:var(--ink);transform:rotate(-7deg);transform-origin:left top}
  .contact li{display:flex;align-items:flex-start;gap:10px;line-height:1.3}
  .contact svg{width:12px;height:12px;margin-top:6px;flex:none;fill:var(--ink)}
  .tagline{position:absolute;right:18px;bottom:52px;transform:rotate(-7deg);font-family:"Quicksand",sans-serif;font-weight:600;font-size:17px;color:#fff}
</style>
</head>
<body>
<main class="sheet">

  <section class="card card--front" aria-label="Business card front">
    <svg class="art" viewBox="0 0 440 440" aria-hidden="true">
      <path d="M0 320 C120 285 270 285 440 320 L440 440 L0 440Z" fill="var(--red)" opacity=".85"/>
      <path d="M0 350 C110 330 220 350 300 440 L0 440Z" fill="var(--blue)"/>
      <path d="M0 385 C80 375 160 395 220 440 L0 440Z" fill="var(--navy)" opacity=".7"/>
      <path d="M440 240 C400 340 300 410 170 440 L440 440Z" fill="var(--orange)" opacity=".9"/>
      <path d="M440 265 C380 360 250 420 90 440 L130 440 C270 420 390 370 440 300Z" fill="var(--yellow)"/>
    </svg>
    <div class="brand-name">
      <span class="mark"></span>
      <span class="line1">BRIGHTWAY</span>
      <span class="line2">Care Partners</span>
    </div>
  </section>

  <section class="card card--back" aria-label="Business card back">
    <svg class="art" viewBox="0 0 440 440" aria-hidden="true">
      <path d="M250 0 L440 0 L440 95 C390 45 320 15 250 0Z" fill="var(--red)"/>
      <path d="M380 0 L440 0 L440 40 C420 22 400 10 380 0Z" fill="var(--orange)"/>
      <path d="M0 70 C80 50 170 25 250 0 L320 0 C210 45 100 95 0 140Z" fill="var(--blue)"/>
      <path d="M320 0 L360 0 C250 55 130 110 0 162 L0 140 C110 92 215 45 320 0Z" fill="var(--yellow)"/>
      <path d="M360 0 L395 0 C280 65 150 120 0 178 L0 162 C130 110 250 55 360 0Z" fill="var(--orange)" opacity=".85"/>
      <path d="M0 365 C120 330 270 325 440 350 L440 440 L0 440Z" fill="var(--red)" opacity=".85"/>
      <path d="M0 390 C110 372 220 388 300 440 L0 440Z" fill="var(--blue)"/>
      <path d="M0 415 C80 408 160 420 220 440 L0 440Z" fill="var(--navy)" opacity=".7"/>
      <path d="M440 240 C400 340 300 410 170 440 L440 440Z" fill="var(--orange)" opacity=".9"/>
      <path d="M440 268 C380 360 250 420 90 440 L130 440 C270 420 390 372 440 305Z" fill="var(--yellow)"/>
    </svg>
    <div class="back-title">BRIGHTWAY</div>
    <div class="kids-area" role="img" aria-label="Faint illustration of four playful children behind the contact details"></div>
    <ul class="contact">
      <li><svg viewBox="0 0 16 16"><path d="M3 1l3 3-2 2c1 2 3 4 5 5l2-2 3 3-2 3C6 15 1 10 1 3z"/></svg>(541) 555-0142</li>
      <li><svg viewBox="0 0 16 16"><path d="M1 3h14v10H1z M1 3l7 6 7-6" stroke="#fff" stroke-width="1"/></svg>jrivera@brightwaycare.com</li>
      <li><svg viewBox="0 0 16 16"><path d="M8 1l7 7h-2v7H3V8H1z"/></svg>www.brightwaycare.com</li>
      <li><svg viewBox="0 0 16 16"><path d="M8 0a5 5 0 0 1 5 5c0 4-5 11-5 11S3 9 3 5a5 5 0 0 1 5-5zm0 3a2 2 0 1 0 0 4 2 2 0 0 0 0-4z"/></svg>4870 Palm Grove Ave, Lakeside,<br>Oregon 97401</li>
    </ul>
    <div class="tagline">Care Partners</div>
  </section>

</main>
</body>
</html>
```